Business card for exciting VC company

Should look simple, crisp, and modern.

Industry/Entity Type

Venture Capital

Contact Information for Business Card

Would like to see at least one design that has our blue on the back with the tagline "Transforming Traditional Industry" and white front with contact details.

Font styles to use
Sans Serif

Requirements
Must have
• Logo

Darius Pellworth
dpellworth@brindlegate.vc
Managing Partner
M (628)304-xxxx

```html
<!DOCTYPE html>
<html lang="en">
<head>
<meta charset="utf-8">
<title>Brindlegate Capital — Business Card</title>
<link rel="stylesheet" href="https://fonts.googleapis.com/css2?family=Lato:wght@400;700&family=Raleway:wght@600;700&display=swap">
<style>
  :root {
    --page-bg: #eeeeee;
    --card-white: #ffffff;
    --brand-blue: #2f78c4;
    --blue-deep: #2a6db5;
    --blue-light: #6ea5d8;
    --ink: #1a1a1a;
    --ink-soft: #4a4a4a;
  }
  * { margin: 0; padding: 0; box-sizing: border-box; }
  html, body {
    width: 1200px; height: 800px; overflow: hidden;
    background: var(--page-bg);
    font-family: "Lato", Arial, sans-serif;
  }
  .canvas { position: relative; width: 1200px; height: 800px; }

  .card { position: absolute; width: 571px; height: 331px; }

  /* Front: white with contact details */
  .card-front { left: 475px; top: 31px; background: var(--card-white); }
  .front-logo {
    position: absolute; left: 48px; top: 134px; width: 226px;
    text-align: center; color: var(--ink); font-weight: 700;
  }
  .front-logo .logo-name { display: block; font-size: 33px; letter-spacing: 1px; line-height: 1; }
  .front-logo .logo-sub { display: block; font-size: 12px; letter-spacing: 4px; margin-top: 6px; }
  .divider {
    position: absolute; left: 287px; top: 107px; width: 2px; height: 118px;
    background: var(--ink);
  }
  .contact { position: absolute; left: 306px; top: 107px; }
  .contact-name {
    font-family: "Raleway", Arial, sans-serif; font-weight: 700;
    color: var(--brand-blue); font-size: 18px; line-height: 22px;
  }
  .contact-title {
    font-family: "Raleway", Arial, sans-serif; font-weight: 600;
    color: var(--ink); font-size: 13.5px; line-height: 18px;
  }
  .contact-list { list-style: none; margin-top: 22px; }
  .contact-list li {
    display: flex; align-items: center; gap: 7px;
    font-size: 17px; line-height: 21.5px; color: var(--ink-soft);
  }
  .contact-list svg { width: 13px; height: 13px; flex: none; }

  /* Back: brand blue with tagline */
  .card-back { left: 170px; top: 405px; overflow: hidden; }
  .back-photo {
    position: absolute; inset: 0;
    background: linear-gradient(125deg, var(--blue-deep) 0%, #3d84c9 45%, var(--blue-light) 100%);
  }
  .back-logo {
    position: absolute; left: 0; right: 0; top: 108px;
    text-align: center; color: var(--card-white); font-weight: 700;
  }
  .back-logo .logo-name { display: block; font-size: 52px; letter-spacing: 3px; line-height: 1; }
  .back-logo .logo-sub { display: block; font-size: 21px; letter-spacing: 7px; margin-top: 12px; }
  .tagline {
    position: absolute; left: 0; right: 0; top: 283px;
    text-align: center; color: var(--card-white);
    font-size: 17px; font-weight: 400; letter-spacing: 0.2px;
  }
</style>
</head>
<body>
<main class="canvas">

  <section class="card card-front" aria-label="Card front">
    <div class="front-logo">
      <span class="logo-name">BRINDLEGATE</span>
      <span class="logo-sub">CAPITAL</span>
    </div>
    <div class="divider"></div>
    <div class="contact">
      <p class="contact-name">Darius Pellworth</p>
      <p class="contact-title">Managing Partner</p>
      <ul class="contact-list">
        <li>
          <svg viewBox="0 0 12 12" aria-hidden="true"><rect x="3" y="0.8" width="6" height="10.4" rx="1.2" fill="none" stroke="var(--brand-blue)" stroke-width="1.3"/><line x1="5" y1="9.3" x2="7" y2="9.3" stroke="var(--brand-blue)" stroke-width="1"/></svg>
          (628)304-xxxx
        </li>
        <li>
          <svg viewBox="0 0 12 12" aria-hidden="true"><rect x="0.8" y="2.5" width="10.4" height="7.5" fill="none" stroke="var(--brand-blue)" stroke-width="1.3"/><polyline points="0.8,2.5 6,7 11.2,2.5" fill="none" stroke="var(--brand-blue)" stroke-width="1.2"/></svg>
          dpellworth@brindlegate.vc
        </li>
        <li>
          <svg viewBox="0 0 12 12" aria-hidden="true"><circle cx="6" cy="6" r="5.2" fill="none" stroke="var(--brand-blue)" stroke-width="1.2"/><ellipse cx="6" cy="6" rx="2.2" ry="5.2" fill="none" stroke="var(--brand-blue)" stroke-width="1"/><line x1="0.8" y1="6" x2="11.2" y2="6" stroke="var(--brand-blue)" stroke-width="1"/></svg>
          BrindlegateCapital.com
        </li>
      </ul>
    </div>
  </section>

  <section class="card card-back" aria-label="Card back">
    <div class="back-photo" role="img" aria-label="Blue-toned upward view of glass office towers and steel framework"></div>
    <div class="back-logo">
      <span class="logo-name">BRINDLEGATE</span>
      <span class="logo-sub">CAPITAL</span>
    </div>
    <p class="tagline">TRANSFORMING TRADITIONAL INDUSTRY</p>
  </section>

</main>
</body>
</html>
```